Unique malt liquor beverage needs a logo design and bottle (6.9oz clear glass flask) label designed.

We need a logo and bottle label design for our new beverage here at Lantern Brewing, a new company based in West Virginia. This is a differentiated product in that we use only natural ingredients and deliver it in a novel 6.9oz glass flask. Our new beverage is a naturally flavored malt liquor drink that we call "Brisket". Our proposed tag line will be "Made to Roar" or "Cold Fizz. Quick Kick". We want a logo and bottle label design that differentiates us even further.

Target Market(s)

See images I uploaded to see our two competitors...we need to be better than this but it gives you idea of the spirit of this beverage class.

Industry/Entity Type

Alcohol beverage

Requirements
Must have
• Label needs to include “14% alc/vol 6.9 oz” Both of these elements can be small and at bottom of front face of label. Also must look great on clear glass flask.
Should not have
• Do not put "malt liquor" on label. Under "Brisket" name it will need to state "Alcoholic Beverage"

```html
<!DOCTYPE html>
<html lang="en">
<head>
<meta charset="utf-8">
<title>Brisket – Bottle Label</title>
<link rel="stylesheet" href="https://fonts.googleapis.com/css2?family=Antonio:wght@400&family=Pinyon+Script&family=Rye&family=Rokkitt:wght@600&family=Arimo:wght@500&display=swap">
<style>
  :root {
    --page: #ffffff;
    --paper-light: #eadab1;
    --paper-dark: #d6be8c;
    --border-dot: #f4f1ea;
    --band-red: #a3121f;
    --band-red-light: #bb2a36;
    --gold: #c98a22;
    --ink: #1e1a16;
    --shadow-red: #5a0810;
    --star: #a58f6a;
    --white: #ffffff;
  }
  html, body {
    margin: 0;
    width: 1200px;
    height: 1200px;
    overflow: hidden;
    background: var(--page);
  }
  .label {
    position: absolute;
    left: 251px;
    top: 60px;
    width: 697px;
    height: 1080px;
  }
  .script { font-family: "Pinyon Script", cursive; fill: var(--ink); }
  .brand-name { font-family: "Rye", serif; fill: var(--band-red); }
  .product-name {
    font-family: "Antonio", sans-serif;
    font-weight: 400;
    fill: var(--white);
    stroke: var(--ink);
    stroke-width: 4;
    paint-order: stroke;
  }
  .product-shadow { font-family: "Antonio", sans-serif; font-weight: 400; fill: var(--shadow-red); }
  .tagline { font-family: "Rokkitt", serif; font-weight: 600; fill: var(--white); letter-spacing: 1px; }
  .stars { fill: var(--star); font-family: "Arimo", sans-serif; letter-spacing: 6px; }
  .category { font-family: "Rye", serif; fill: var(--ink); }
  .origin { font-family: "Rye", serif; fill: var(--ink); letter-spacing: 3px; }
  .spec { font-family: "Arimo", sans-serif; font-weight: 500; fill: var(--ink); }
</style>
</head>
<body>
<svg class="label" viewBox="0 0 697 1080" xmlns="http://www.w3.org/2000/svg">
  <defs>
    <linearGradient id="paper" x1="0" y1="0" x2="1" y2="1">
      <stop offset="0" stop-color="var(--paper-light)"/>
      <stop offset="0.55" stop-color="var(--paper-dark)"/>
      <stop offset="1" stop-color="var(--paper-light)"/>
    </linearGradient>
    <linearGradient id="band" x1="0" y1="0" x2="1" y2="0">
      <stop offset="0" stop-color="var(--band-red)"/>
      <stop offset="0.25" stop-color="var(--band-red-light)"/>
      <stop offset="1" stop-color="var(--band-red)"/>
    </linearGradient>
  </defs>

  <rect class="paper" width="697" height="1080" fill="url(#paper)"/>

  <rect class="dotted-frame" x="53" y="77" width="602" height="944" fill="none"
        stroke="var(--border-dot)" stroke-width="5" stroke-dasharray="7 9"/>

  <rect role="img" aria-label="Flourish ornament above flavour note" x="125" y="128" width="190" height="22" rx="11" fill="var(--paper-dark)" opacity="0.7"/>
  <text class="script" x="218" y="222" font-size="56" text-anchor="middle">Naturally</text>
  <text class="script" x="218" y="275" font-size="56" text-anchor="middle">Flavored</text>
  <rect role="img" aria-label="Flourish ornament below flavour note" x="125" y="292" width="190" height="22" rx="11" fill="var(--paper-dark)" opacity="0.7"/>

  <circle class="maker-dot" cx="490" cy="150" r="22" fill="var(--band-red)"/>
  <text class="brand-name" x="490" y="215" font-size="30" text-anchor="middle">Lantern</text>
  <text class="brand-name" x="490" y="252" font-size="30" text-anchor="middle">Brewing</text>

  <polygon class="band-gold-top" points="0,405 697,236 697,261 0,430" fill="var(--gold)"/>
  <polygon class="band-red" points="0,430 697,261 697,531 0,714" fill="url(#band)"/>
  <polygon class="band-gold-bottom" points="0,714 697,531 697,555 0,738" fill="var(--gold)"/>

  <g transform="translate(350 520) rotate(-14)">
    <text class="product-shadow" x="-7" y="66" font-size="190" text-anchor="middle" textLength="560" lengthAdjust="spacingAndGlyphs">BRISKET</text>
    <text class="product-name" x="0" y="59" font-size="190" text-anchor="middle" textLength="560" lengthAdjust="spacingAndGlyphs">BRISKET</text>
  </g>

  <rect class="tag" x="165" y="661" width="387" height="74" fill="var(--ink)"/>
  <text class="tagline" x="358" y="710" font-size="40" text-anchor="middle">MADE TO ROAR</text>

  <text class="stars" x="361" y="786" font-size="20" text-anchor="middle">★★★★★★★</text>
  <text class="category" x="358" y="843" font-size="40" text-anchor="middle" textLength="460" lengthAdjust="spacingAndGlyphs">ALCOHOLIC BEVERAGE</text>
  <text class="stars" x="361" y="884" font-size="20" text-anchor="middle">★★★★★★★</text>

  <text class="origin" x="358" y="950" font-size="40" text-anchor="middle">WEST</text>
  <text class="origin" x="358" y="996" font-size="40" text-anchor="middle">VIRGINIA</text>
  <text class="spec" x="83" y="960" font-size="30">14%</text>
  <text class="spec" x="83" y="993" font-size="30">alc/vol</text>
  <text class="spec" x="603" y="960" font-size="30" text-anchor="middle">6.9</text>
  <text class="spec" x="603" y="993" font-size="30" text-anchor="middle">oz</text>
</svg>
</body>
</html>
```